One page sales fact sheet for data consultancy company

We need a serious and professional looking 1-page fact sheet that we want to send over to potential clients via email.
The upper part should consists of a header, the client logo and 3 charts.
(1 chart with 5 datapoints / 1 chart with 3 bubbles and percentage in it, 1 chart with numbers and text)
In the lower part there should be some text description about our company and a big chart consisting of a table (see drawing).
See attached drawing to get a better understanding of the whole idea.
The fact sheet should be catchy but professional in the same way.
Colors your choice but classic, i.e. black/white/grey/blue
The contest winner can expect more work from us based on the winning design.
*Please note that the logo reflects our original logo style but is not our
actual company name for privacy reasons

```html
<!DOCTYPE html>
<html lang="en">
<head>
<meta charset="utf-8">
<title>Voran Market Analysis Fact Sheet</title>
<link href="https://fonts.googleapis.com/css2?family=Montserrat:wght@400;500;600;700;800&display=swap" rel="stylesheet">
<style>
:root{
  --blue:#2433b6;
  --blue-dark:#1a2590;
  --black:#1c1c1e;
  --grey:#676767;
  --grey-light:#e3e3e3;
  --line:#c9c9c9;
  --white:#ffffff;
  --text:#1f1f1f;
  --bg:#e9eaee;
}
*{box-sizing:border-box;margin:0;padding:0}
html,body{width:1200px;height:613px;overflow:hidden;background:var(--bg);font-family:"Montserrat",Arial,sans-serif;color:var(--text)}
.sheet{position:absolute;left:395px;top:16px;width:410px;height:580px;background:var(--white);box-shadow:0 6px 18px rgba(0,0,0,.18);overflow:hidden}
.header{position:absolute;left:0;top:0;width:410px;height:90px}
.brand{position:absolute;left:20px;top:19px;font-weight:800;font-size:30px;color:var(--white);letter-spacing:1px}
.title{position:absolute;right:13px;top:12px;text-align:right;font-weight:800;font-size:22px;line-height:.9;color:var(--white)}
.panel{position:absolute;border:1.5px solid var(--line);border-radius:9px;overflow:hidden;background:var(--white)}
.panel-head{height:28px;color:var(--white);font-weight:700;font-size:15.5px;letter-spacing:.6px;display:flex;align-items:center;justify-content:center;border-radius:8px 8px 0 0}
.panel-head.blue{background:linear-gradient(90deg,var(--blue-dark),var(--blue))}
.panel-head.grey{background:linear-gradient(90deg,#5d5d5d,#7a7a7a)}
.datapoints{left:9px;top:92px;width:189px;height:134px}
.points{list-style:none;padding-top:3px}
.points li{display:flex;align-items:flex-start;gap:6px;font-size:6.6px;font-weight:600;line-height:1.35;padding:2.5px 8px}
.points li:nth-child(even){background:#ececec}
.points svg{flex:none;margin-top:1px}
.product{left:208px;top:92px;width:189px;height:134px}
.bubbles{display:flex;padding-top:12px}
.bubble-col{flex:1;text-align:center;border-left:1px solid #ddd;height:90px}
.bubble-col:first-child{border-left:none}
.bubble{width:47px;height:47px;border-radius:50%;margin:0 auto 7px;display:flex;align-items:center;justify-content:center;color:var(--white);font-weight:600;font-size:17px}
.b-blue{background:radial-gradient(circle at 40% 30%,#3d4fe0,#1a2590 75%)}
.b-dark{background:radial-gradient(circle at 40% 30%,#6a6a6a,#1e1e1e 75%)}
.b-light{background:radial-gradient(circle at 40% 30%,#e0e0e0,#8f8f8f 80%)}
.bubble-col p{font-size:6.4px;font-weight:500;line-height:1.3}
.stats{left:9px;top:234px;width:390px;height:115px}
.stat-row{display:flex;height:81px}
.stat{text-align:center;border-left:1px solid #ddd;padding-top:6px}
.stat:first-child{border-left:none}
.stat .num{color:var(--blue);font-weight:800;font-size:31px;line-height:1;margin-top:2px}
.stat .lbl{font-weight:600;font-size:8px;margin-top:3px}
.sales{height:34px;background:var(--grey-light);display:flex;align-items:center;justify-content:center;font-weight:800;font-size:22px}
.about{position:absolute;left:14px;top:361px;width:382px;text-align:center;font-size:6.8px;line-height:1.38}
.about p+p{margin-top:4px}
.step-band{position:absolute;left:0;top:427px;width:410px;height:29px;background:linear-gradient(90deg,var(--blue-dark),var(--blue),var(--blue-dark));color:var(--white);font-weight:700;font-size:20px;display:flex;align-items:center;justify-content:center}
.layers{position:absolute;left:84px;top:468px;width:250px}
.layer{display:flex;height:21px;margin-bottom:3.6px;border:1px solid var(--line)}
.layer-name{width:107px;color:var(--white);font-weight:700;font-size:12px;display:flex;align-items:center;justify-content:center}
.layer:nth-child(odd) .layer-name{background:var(--blue)}
.layer:nth-child(even) .layer-name{background:var(--grey)}
.layer-value{flex:1;font-weight:700;font-size:12.5px;display:flex;align-items:center;padding-left:14px}
</style>
</head>
<body>
<main class="sheet">
  <header class="header">
    <svg width="410" height="90" viewBox="0 0 410 90" aria-hidden="true">
      <polygon points="0,0 410,0 410,28 0,82" fill="#1c1c1e"/>
      <polygon points="0,82 220,46 225,48 0,86" fill="#cfcfcf"/>
      <polygon points="262,0 410,0 410,85 150,41" fill="#2433b6"/>
    </svg>
    <div class="brand">VORAN</div>
    <h1 class="title">MARKET<br>ANALYSIS</h1>
  </header>

  <section class="panel datapoints">
    <h2 class="panel-head blue">5 DATAPOINTS</h2>
    <ul class="points">
      <li><svg width="7" height="7" viewBox="0 0 10 10"><circle cx="5" cy="5" r="4.2" fill="none" stroke="#222" stroke-width="1.2"/><path d="M3 5.2l1.5 1.5L7.2 3.8" fill="none" stroke="#222" stroke-width="1.2"/></svg>Lorem Ipsum is simply dummy text</li>
      <li><svg width="7" height="7" viewBox="0 0 10 10"><circle cx="5" cy="5" r="4.2" fill="none" stroke="#222" stroke-width="1.2"/><path d="M3 5.2l1.5 1.5L7.2 3.8" fill="none" stroke="#222" stroke-width="1.2"/></svg>Printing and typesetting industry. Lorem Ipsum has been the industry's.</li>
      <li><svg width="7" height="7" viewBox="0 0 10 10"><circle cx="5" cy="5" r="4.2" fill="none" stroke="#222" stroke-width="1.2"/><path d="M3 5.2l1.5 1.5L7.2 3.8" fill="none" stroke="#222" stroke-width="1.2"/></svg>Standard dummy text ever since the 1500s, when an unknown printer</li>
      <li><svg width="7" height="7" viewBox="0 0 10 10"><circle cx="5" cy="5" r="4.2" fill="none" stroke="#222" stroke-width="1.2"/><path d="M3 5.2l1.5 1.5L7.2 3.8" fill="none" stroke="#222" stroke-width="1.2"/></svg>Took a galley of type and scrambled it to make a type specimen book.</li>
      <li><svg width="7" height="7" viewBox="0 0 10 10"><circle cx="5" cy="5" r="4.2" fill="none" stroke="#222" stroke-width="1.2"/><path d="M3 5.2l1.5 1.5L7.2 3.8" fill="none" stroke="#222" stroke-width="1.2"/></svg>Lorem Ipsum is simply dummy text</li>
    </ul>
  </section>

  <section class="panel product">
    <h2 class="panel-head grey">PRODUCT TYPE</h2>
    <div class="bubbles">
      <div class="bubble-col"><div class="bubble b-blue">40%</div><p>Lorem Ipsum<br>simply dummy<br>text</p></div>
      <div class="bubble-col"><div class="bubble b-dark">30%</div><p>Lorem Ipsum<br>simply dummy<br>text</p></div>
      <div class="bubble-col"><div class="bubble b-light">20%</div><p>Lorem Ipsum<br>simply dummy<br>text</p></div>
    </div>
  </section>

  <section class="panel stats">
    <div class="stat-row">
      <div class="stat" style="width:93px">
        <svg width="18" height="20" viewBox="0 0 18 20" aria-hidden="true"><circle cx="9" cy="3" r="2.4" fill="#8a8a8a"/><path d="M4 10c0-3 2-5 5-5s5 2 5 5v2H4z" fill="#8a8a8a"/><rect x="3" y="11" width="12" height="3" rx="1.5" fill="#8a8a8a"/><path d="M6 14v5M12 14v5" stroke="#8a8a8a" stroke-width="1.5"/></svg>
        <div class="num">20</div><div class="lbl">VENDORS</div>
      </div>
      <div class="stat" style="width:106px">
        <svg width="22" height="20" viewBox="0 0 22 20" aria-hidden="true"><path d="M11 2l8 4v9l-8 4-8-4V6z" fill="none" stroke="#8a8a8a" stroke-width="1.5"/><path d="M3 6l8 4 8-4M11 10v9" fill="none" stroke="#8a8a8a" stroke-width="1.5"/></svg>
        <div class="num">150</div><div class="lbl">PRODUCT</div>
      </div>
      <div class="stat" style="flex:1">
        <svg width="22" height="20" viewBox="0 0 22 20" aria-hidden="true"><path d="M18 6a8 8 0 1 0 1 6" fill="none" stroke="#8a8a8a" stroke-width="1.4"/><path d="M16 3l3 3-4 1" fill="none" stroke="#8a8a8a" stroke-width="1.4"/><path d="M11 6l4 2v4l-4 2-4-2V8z" fill="none" stroke="#8a8a8a" stroke-width="1.2"/></svg>
        <div class="num">350,000</div><div class="lbl">AVAILABLE ITEMS</div>
      </div>
    </div>
    <div class="sales">40 MLN IN SALES</div>
  </section>

  <section class="about">
    <p>Lorem Ipsum is simply dummy text of the printing and typesetting industry. Lorem Ipsum has been the industry's standard dummy text ever since the 1500s, when an unknown printer took a galley of type and scrambled it to make a type specimen book.</p>
    <p>Lorem Ipsum is simply dummy text of the printing and typesetting industry. Lorem Ipsum has been the industry's standard dummy text ever since the 1500s, .</p>
  </section>

  <h2 class="step-band">STEP</h2>

  <section class="layers">
    <div class="layer"><div class="layer-name">LAYER 1</div><div class="layer-value">COMPETITORS</div></div>
    <div class="layer"><div class="layer-name">LAYER 2</div><div class="layer-value">USER LEVEL</div></div>
    <div class="layer"><div class="layer-name">LAYER 3</div><div class="layer-value">EMITY LEVEL</div></div>
    <div class="layer"><div class="layer-name">LAYER 4</div><div class="layer-value">PERSONAL LEVEL</div></div>
  </section>
</main>
</body>
</html>
```